BrightPath Medical Exercise, LLC specializes in post rehab medical exercise for clients who have been discharged from physical therapy and/or other medical services and are in need of continued cardiovascular, strength, flexibility, endurance training and management of their medical conditions. We strive to bridge the gap between healthcare and fitness by staying in communication with the referring physician and /or physical therapist with updated progress notes to follow each clients progression, making sure each client is appropriate for exercise and identifying any red flags throughout the initial assessment and screening of the client, and referring those clients back to the physician and/or therapist when necessary.
Colors
Designer to choose colors to be used in the design.
Requirements
Must have
- Pictures of a trainer working with a client one on one during exercise, and group exercise
Nice to have
- Pictures that portray the bridge between healthcare and fitness
Should not have
- Cursive writing

```html
<!DOCTYPE html>
<html lang="en">
<head>
<meta charset="utf-8">
<title>BrightPath Medical Exercise – Rack Card</title>
<link href="https://fonts.googleapis.com/css2?family=Montserrat:wght@400;600;700;800&display=swap" rel="stylesheet">
<style>
  :root {
    --red: #c8242b;
    --red-bright: #ee4c45;
    --red-deep: #9b1a20;
    --ink: #1d1d1d;
    --paper: #ffffff;
    --backdrop: #e6e6e6;
    --photo-light: #eeece6;
    --photo-mid: #d9d2c4;
  }
  * { box-sizing: border-box; margin: 0; padding: 0; }
  html, body {
    width: 1200px; height: 1177px; overflow: hidden;
    background: var(--backdrop);
    font-family: "Montserrat", sans-serif;
  }
  .rack-card {
    position: absolute; left: 330px; top: 18px;
    width: 540px; height: 1140px;
    background: var(--paper);
    box-shadow: 0 6px 24px rgba(0,0,0,.18);
    overflow: hidden;
  }
  .brand-mark {
    position: absolute; top: 40px; left: 0; width: 100%;
    display: flex; flex-direction: column; align-items: center; gap: 14px;
  }
  .brand-mark .dot {
    width: 96px; height: 96px; border-radius: 50%;
    border: 5px solid var(--red-bright);
  }
  .brand-mark .name {
    font-weight: 700; font-size: 13px; letter-spacing: .5px;
    color: var(--ink); text-align: center; line-height: 1.25;
  }
  .hero { position: absolute; top: 180px; left: 0; width: 540px; height: 320px; }
  .services {
    position: absolute; top: 520px; left: 30px; right: 30px;
    text-align: center; color: var(--ink);
  }
  .services h2 {
    color: var(--red); font-weight: 800; font-size: 22px;
    letter-spacing: .5px; margin-bottom: 8px;
  }
  .services .offer { font-size: 13px; line-height: 1.35; }
  .services .quote {
    font-weight: 700; font-size: 13px; line-height: 1.35; margin-top: 12px;
  }
  .services .quote .author { color: var(--red); }
  .services .lead { font-weight: 700; font-size: 13.5px; margin-top: 14px; }
  .conditions {
    position: absolute; top: 720px; left: 20px; right: 20px;
    display: grid; grid-template-columns: 1fr 1fr; column-gap: 26px;
    color: var(--red); font-weight: 700; font-size: 14.5px; line-height: 19px;
  }
  .conditions ul { list-style: none; }
  .conditions .col-left { text-align: right; }
  .conditions .col-right { text-align: left; }
  .footer-band { position: absolute; left: 0; bottom: 0; width: 540px; height: 150px; }
  .footer-text {
    position: absolute; left: 0; bottom: 22px; width: 100%;
    text-align: center; color: var(--paper);
    font-weight: 700; font-size: 15px; line-height: 1.4;
  }
</style>
</head>
<body>
  <div class="rack-card">
    <div class="brand-mark">
      <div class="dot"></div>
      <div class="name">BRIGHTPATH<br>MEDICAL EXERCISE</div>
    </div>

    <svg class="hero" viewBox="0 0 540 320">
      <defs>
        <linearGradient id="photoTone" x1="0" y1="0" x2="0" y2="1">
          <stop offset="0" stop-color="var(--photo-light)"/>
          <stop offset="1" stop-color="var(--photo-mid)"/>
        </linearGradient>
      </defs>
      <polyline points="0,8 270,28 540,8" fill="none" stroke="var(--red-bright)" stroke-width="8"/>
      <polyline points="0,20 270,40 540,20" fill="none" stroke="var(--ink)" stroke-width="6"/>
      <polygon role="img" aria-label="Photo of a woman standing in a sunlit field with arms spread wide"
               points="0,26 270,46 540,26 540,262 270,292 0,262" fill="url(#photoTone)"/>
      <polyline points="0,266 270,296 540,266" fill="none" stroke="var(--ink)" stroke-width="6"/>
      <polyline points="0,280 270,310 540,280" fill="none" stroke="var(--red-bright)" stroke-width="8"/>
    </svg>

    <section class="services">
      <h2>OUR PRODUCTS AND SERVICES:</h2>
      <p class="offer">Initial Assessment and Functional Screening<br>
        One-On-One supervised post rehab exercise<br>
        Online consultation with individualized home exercise program</p>
      <p class="quote">“Exercise is the key to long-term management of most medical conditions” ~ <span class="author">Daniel R Hayes,</span><br>PhD, PT</p>
      <p class="lead">We offer management of the following conditions and more:</p>
    </section>

    <div class="conditions">
      <ul class="col-left">
        <li>Diabetes</li><li>Hypertension</li><li>ACL Rupture</li><li>Ankle Fracture</li>
        <li>Bicipital Tendonitis</li><li>Total Hip Replacement</li><li>Total Knee Replacement</li>
        <li>Spinal Stenosis</li><li>Multiple Sclerosis</li><li>Shoulder Dislocation</li>
        <li>Scoliosis</li><li>Osteoporosis</li><li>Osteoarthritis</li><li>Cervical disc herniation</li>
      </ul>
      <ul class="col-right">
        <li>AC Joint Separation</li><li>Fibromyalgia</li><li>Spondylothesis</li><li>Parkinson’s Disease</li>
        <li>Tibial Plateau Fracture</li><li>Tennis Elbow/Golfer’s Elbow</li><li>Carpal Tunnel Syndrome</li>
        <li>Total Shoulder Replacement</li><li>Bicipital Tendonitis</li><li>Patello-Femoral Syndrome</li>
        <li>Rotator Cuff Syndrome</li><li>Cervical Strain</li><li>Impingement Syndrome</li><li>Laminectomy</li>
      </ul>
    </div>

    <svg class="footer-band" viewBox="0 0 540 150">
      <defs>
        <linearGradient id="bandTone" x1="0" y1="0" x2="1" y2="0">
          <stop offset="0" stop-color="var(--red-deep)"/>
          <stop offset=".5" stop-color="var(--red-bright)"/>
          <stop offset="1" stop-color="var(--red-deep)"/>
        </linearGradient>
      </defs>
      <polyline points="0,12 300,6 540,34" fill="none" stroke="var(--ink)" stroke-width="6"/>
      <polygon points="0,26 300,20 540,48 540,150 0,150" fill="url(#bandTone)"/>
    </svg>
    <div class="footer-text">
      BRIGHTPATH MEDICAL EXERCISE, LLC<br>
      “Getting You Back To Function As Quickly And<br>Safely As Possible”
    </div>
  </div>
</body>
</html>
```